Modern Warmth + Professional Balance Florfenicol Spray 5% packaging desgin

Size:40mm*40mm*154mm(H)
Product: Florfenicol Spray 5%(animal health)
Design Style: Please refer to the brand style of Quelmar and other international animal health companies to design a professional, clean, and trustworthy package for a pet topical spray. The information hierarchy should be clear, and the design should be suitable for the global market.

Target Market(s)

global market

Industry/Entity Type

veterinary drug

Colors
0054AA
0677BA
7BADD7
CADEEF
E8F1F8
0094D4
00A9DD
6FCCEA
C7EBF8
E9F6FB
00AB8E
00BBA5
67D7C9
C6EFE9
E9F9F6
59FF00
82FF00
B8FF75
E3FFCB
F4FFEA
EE7325
F08F49
F5BC92
FAE3D3
FDF4ED

```html
<!DOCTYPE html>
<html lang="en">
<head>
<meta charset="utf-8">
<title>Veltacin Florfenicol Spray 5% – Carton Dieline</title>
<link rel="stylesheet" href="https://fonts.googleapis.com/css2?family=Montserrat:ital,wght@0,600;1,400;1,700&family=Oswald:wght@700&family=Roboto:wght@400;500;700&display=swap">
<style>
  :root {
    --navy: #0b3a8b;
    --navy-deep: #08327c;
    --lime: #8bd52c;
    --white: #ffffff;
    --paper: #ffffff;
    --cut-line: #8a8a8a;
    --photo-light: #e9d6b8;
    --photo-dark: #b58a55;
  }
  html, body {
    margin: 0;
    padding: 0;
    width: 1044px;
    height: 1200px;
    overflow: hidden;
    background: var(--paper);
  }
  .dieline { display: block; width: 1044px; height: 1200px; }
  .fill-navy { fill: var(--navy); }
  .fill-lime { fill: var(--lime); }
  .fill-white { fill: var(--white); }
  .glue-flap { fill: var(--white); stroke: var(--cut-line); stroke-width: 1.5; }
  .brand-name { font-family: "Oswald", sans-serif; font-weight: 700; fill: var(--navy); font-size: 62px; }
  .brand-tm { font-family: "Roboto", sans-serif; font-weight: 500; fill: #222; font-size: 16px; }
  .product-name { font-family: "Oswald", sans-serif; font-weight: 700; fill: var(--white); font-size: 46px; }
  .volume { font-family: "Montserrat", sans-serif; font-weight: 600; fill: var(--white); font-size: 30px; letter-spacing: 1px; }
  .species { font-family: "Montserrat", sans-serif; font-style: italic; fill: var(--navy); font-size: 23px; }
  .species .strong { font-weight: 700; }
  .caution-box { fill: none; stroke: var(--lime); stroke-width: 3; }
  .caution-text { font-family: "Roboto", sans-serif; font-weight: 500; fill: var(--white); font-size: 17.5px; }
  .maker-mark { font-family: "Montserrat", sans-serif; font-weight: 600; fill: var(--white); font-size: 40px; letter-spacing: 2px; }
  .section-title { font-family: "Roboto", sans-serif; font-weight: 700; fill: var(--white); font-size: 24px; }
  .body-text { font-family: "Roboto", sans-serif; font-weight: 400; fill: var(--white); font-size: 17px; }
  .lead-text { font-family: "Roboto", sans-serif; font-weight: 400; fill: var(--white); font-size: 19px; }
  .maker-detail { font-family: "Roboto", sans-serif; font-weight: 700; fill: var(--white); font-size: 14px; }
  .vet-use { font-family: "Roboto", sans-serif; font-weight: 700; font-style: italic; fill: var(--white); font-size: 21px; }
</style>
</head>
<body>
<svg class="dieline" viewBox="0 0 1790 2100" preserveAspectRatio="xMidYMid meet" xmlns="http://www.w3.org/2000/svg">
  <defs>
    <linearGradient id="photoTone" x1="0" y1="0" x2="1" y2="0">
      <stop offset="0" stop-color="#d9b27a"/>
      <stop offset="0.45" stop-color="#9c7650"/>
      <stop offset="1" stop-color="#e6d8c8"/>
    </linearGradient>
    <g id="front-face">
      <rect class="fill-white" x="0" y="0" width="276" height="1062"/>
      <text class="brand-name" x="28" y="155">Veltacin</text>
      <text class="brand-tm" x="222" y="107">TM</text>
      <rect class="fill-lime" x="0" y="195" width="276" height="129"/>
      <text class="product-name" text-anchor="middle" x="138" y="253">FLORFENICOL</text>
      <text class="product-name" text-anchor="middle" x="138" y="300">SPRAY 5%</text>
      <polygon class="fill-navy" points="0,324 147,324 135,362 0,362"/>
      <text class="volume" x="22" y="354">100ml</text>
      <text class="species" text-anchor="middle" x="138" y="413">For <tspan class="strong">Dogs,</tspan></text>
      <text class="species" text-anchor="middle" x="138" y="445"><tspan class="strong">Cats, Fur Animals</tspan></text>
      <rect x="0" y="472" width="276" height="212" fill="url(#photoTone)" rx="4" role="img" aria-label="Photo of a golden retriever, a tabby cat and a lop-eared rabbit sitting together"/>
      <polygon class="fill-lime" points="0,767 276,697 276,757 0,822"/>
      <polygon class="fill-white" points="22,792 250,737 250,760 22,815"/>
      <polygon class="fill-navy" points="0,822 276,757 276,1062 0,1062"/>
      <rect class="caution-box" x="40" y="858" width="196" height="82" rx="3"/>
      <text class="caution-text" text-anchor="middle" x="138" y="884">CAUTION: Pregnant</text>
      <text class="caution-text" text-anchor="middle" x="138" y="905">pets and Collie should</text>
      <text class="caution-text" text-anchor="middle" x="138" y="926">use it carefully</text>
      <text class="maker-mark" text-anchor="middle" x="138" y="1028">NORVANE</text>
    </g>
  </defs>

  <!-- top flaps -->
  <path class="fill-navy" d="M302,498 V375 H520 Q548,375 552,410 L558,485 L568,498 Z"/>
  <path class="fill-navy" d="M1110,498 V375 H892 Q864,375 860,410 L854,485 L844,498 Z"/>
  <path class="fill-navy" d="M1120,222 V175 Q1120,120 1175,120 H1341 Q1396,120 1396,175 V222 Z"/>
  <rect class="fill-white" x="1120" y="222" width="276" height="276"/>
  <g transform="rotate(180 1258 360)">
    <text class="brand-name" x="1166" y="290">Veltacin</text>
    <text class="brand-tm" x="1360" y="242">TM</text>
    <rect class="fill-lime" x="1120" y="310" width="276" height="128"/>
    <text class="product-name" text-anchor="middle" x="1258" y="367">FLORFENICOL</text>
    <text class="product-name" text-anchor="middle" x="1258" y="414">SPRAY 5%</text>
    <polygon class="fill-navy" points="1120,438 1266,438 1255,478 1120,478"/>
    <text class="volume" x="1142" y="469">100ml</text>
  </g>

  <!-- bottom flaps -->
  <path class="fill-navy" d="M302,1560 L310,1640 Q315,1685 345,1685 H558 V1560 Z"/>
  <path class="fill-navy" d="M568,1560 H844 V1885 Q844,1940 789,1940 H623 Q568,1940 568,1885 Z"/>
  <line x1="568" y1="1835" x2="844" y2="1835" stroke="#062c6c" stroke-width="2"/>
  <path class="fill-navy" d="M1110,1560 L1102,1640 Q1097,1685 1067,1685 H855 V1560 Z"/>

  <!-- glue flap -->
  <polygon class="glue-flap" points="1396,498 1500,518 1500,1540 1396,1560"/>

  <!-- side panel: composition & usage -->
  <g class="side-panel-info">
    <rect class="fill-navy" x="292" y="498" width="276" height="1062"/>
    <text class="section-title" x="315" y="560">Composition</text>
    <text class="lead-text" x="319" y="595">Each ml contains:</text>
    <text class="lead-text" x="319" y="628">Florfenicol.........50mg</text>
    <text class="section-title" x="315" y="675">Indication</text>
    <text class="body-text" x="313" y="706">
      <tspan x="313" dy="0">Prevents and treats a series</tspan>
      <tspan x="313" dy="22.5">of skin inflammations caused</tspan>
      <tspan x="313" dy="22.5">by bacteria, ringworm, hair</tspan>
      <tspan x="313" dy="22.5">follicle infection and</tspan>
      <tspan x="313" dy="22.5">allergens in the skin of dogs,</tspan>
      <tspan x="313" dy="22.5">cats, rabbits and other fur</tspan>
      <tspan x="313" dy="22.5">animals. Common clinical</tspan>
      <tspan x="313" dy="22.5">symptoms such as skin</tspan>
      <tspan x="313" dy="22.5">erythema, itching, red and</tspan>
      <tspan x="313" dy="22.5">swollen hair follicles, papules,</tspan>
      <tspan x="313" dy="22.5">hair loss, scaly, pus swelling</tspan>
      <tspan x="313" dy="22.5">between the toes, etc.</tspan>
    </text>
    <text class="section-title" x="313" y="1010">Administration</text>
    <text class="section-title" x="313" y="1040">And dosage</text>
    <text class="body-text" x="313" y="1074">
      <tspan x="313" dy="0">For external use, spray on the</tspan>
      <tspan x="313" dy="22.5">cleansed skin of the affected</tspan>
      <tspan x="313" dy="22.5">area, use 2 to 3 times a day</tspan>
      <tspan x="313" dy="22.5">for 7 to 10 days. or follow the</tspan>
      <tspan x="313" dy="22.5">doctor’s advice.</tspan>
    </text>
    <text class="section-title" x="313" y="1205">Adverse Reaction</text>
    <text class="body-text" x="313" y="1237">
      <tspan x="313" dy="0">Occasionally,transient skin</tspan>
      <tspan x="313" dy="22.5">allergic reactions,such as</tspan>
      <tspan x="313" dy="22.5">itching,redness and</tspan>
      <tspan x="313" dy="22.5">swelling,usually return to</tspan>
      <tspan x="313" dy="22.5">normal within 10 minutes.</tspan>
    </text>
    <text class="section-title" x="315" y="1394">Manufacturer:</text>
    <text class="maker-detail" x="316" y="1418">Norvane Animal Health Co. Ltd</text>
    <text class="maker-detail" x="316" y="1438">www.norvanevet.com</text>
    <text class="vet-use" x="327" y="1512">For Veterinary Use</text>
  </g>

  <!-- front panels -->
  <use href="#front-face" x="568" y="498"/>
  <use href="#front-face" x="1120" y="498"/>

  <!-- side panel: precautions -->
  <g class="side-panel-precautions">
    <rect class="fill-navy" x="844" y="498" width="276" height="1062"/>
    <text class="section-title" x="864" y="570">Precautions</text>
    <text class="body-text" x="865" y="606">
      <tspan x="865" dy="0">1. This products is an</tspan>
      <tspan x="865" dy="22.5">antibacterial and anti-</tspan>
      <tspan x="865" dy="22.5">inflammatory drug for pets. it</tspan>
      <tspan x="865" dy="22.5">is necessary to avoid the</tspan>
      <tspan x="865" dy="22.5">liquid contacting the eyes</tspan>
      <tspan x="865" dy="22.5">during use. it  safe for pets to</tspan>
      <tspan x="865" dy="22.5">lick a little without side</tspan>
      <tspan x="865" dy="22.5">effects.</tspan>
    </text>
    <text class="body-text" x="865" y="803">
      <tspan x="865" dy="0">2. If there is an allergic</tspan>
      <tspan x="865" dy="22.5">reaction at the medication</tspan>
      <tspan x="865" dy="22.5">site. the medication should be</tspan>
      <tspan x="865" dy="22.5">discontinued immediately. it</tspan>
      <tspan x="865" dy="22.5">lasts for a long time, consult a</tspan>
      <tspan x="865" dy="22.5">physician.</tspan>
    </text>
    <text class="body-text" x="865" y="955">
      <tspan x="865" dy="0">3. Use with caution during</tspan>
      <tspan x="865" dy="22.5">pregnancy, lactation and</tspan>
      <tspan x="865" dy="22.5">vaccination period.</tspan>
    </text>
    <text class="body-text" x="863" y="1038">
      <tspan x="863" dy="0">4. For pets with liver and</tspan>
      <tspan x="863" dy="22.5">kidney dysfunction, the dosage</tspan>
      <tspan x="863" dy="22.5">should be appropriately</tspan>
      <tspan x="863" dy="22.5">reduced or the interval</tspan>
      <tspan x="863" dy="22.5">between administrations</tspan>
      <tspan x="863" dy="22.5">should be prolonged.</tspan>
    </text>
    <text class="body-text" x="865" y="1190">
      <tspan x="865" dy="0">5. Please keep this product</tspan>
      <tspan x="865" dy="22.5">out of reach of children.</tspan>
    </text>
    <text class="body-text" x="865" y="1250">
      <tspan x="865" dy="0">6. Do not incinerate or</tspan>
      <tspan x="865" dy="22.5">puncture the spraycan.</tspan>
    </text>
    <text class="section-title" x="864" y="1319">Withdrawal Time</text>
    <text class="body-text" x="864" y="1347">
      <tspan x="864" dy="0">No need to be formulated for</tspan>
      <tspan x="864" dy="22.5">non-food animals</tspan>
    </text>
    <text class="section-title" x="864" y="1398">Storage</text>
    <text class="body-text" x="864" y="1423">
      <tspan x="864" dy="0">Tightly sealed and protect</tspan>
      <tspan x="864" dy="22.5">from light.</tspan>
    </text>
    <text class="section-title" x="863" y="1476">Expired Time :</text>
    <text class="body-text" x="864" y="1504">3 years</text>
  </g>
</svg>
</body>
</html>
```